Sophisticated, clean website reflecting my feminine, playful side to sell my abstract art,

I need a website no more than 3 pages to showcase my paintings, a little about me and some contact info. I do abstracts so looking for something a little edgy, yet feminine and current.
Updates

Hi there, These are some artists websites that I Iike: Mirabelvoss.com (I like how airy it is) tobiasmerrowind.com kevinplodderas.com (I like how it scrolls) I'll need a place for a photo ( a headshot-i do not have it yet so I'll need to be able to upload that later) as well as an area for my bio. Also, it's important that I will be able to upload any new photos and descriptions easily so it should be user friendly. Lastly, I like in a sunny place so would like to have this seem upbeat and playful as that is how i like to paint. thanks-I'm trying to upload my photos now -

Target Market(s)

ppl ages 35-70 who want large scale art for their homes

Industry/Entity Type

art

Coding

Coded - Design and coding required

Number of Pages Required

3 page

Colors

Designer to choose colors to be used in the design.

Requirements
Must have
• photos of my art, a place for my bio, be easy to reach me. tasteful-nothing too "in your face" -my clients are pretty high end and organized. They like clean lines
Nice to have
• sophisticated background, muted tones in the back-similar clean font throughout-no cursive
Should not have
• too many dark areas. Too many blocks of color. Too serious.

```html
<!DOCTYPE html>
<html lang="en">
<head>
<meta charset="utf-8">
<title>Marlena Voskuijl — Abstract Art</title>
<link href="https://fonts.googleapis.com/css2?family=Oswald:wght@300;400&display=swap" rel="stylesheet">
<style>
  :root {
    --ink: #1c1c1a;
    --gold: #bdb68e;
    --gold-deep: #9a8a55;
    --accent: #8c7a4b;
    --wood: #4a2612;
    --wood-light: #7a4a2c;
    --mat: #f1f1f1;
    --paper: #ffffff;
  }
  * { box-sizing: border-box; margin: 0; padding: 0; }
  html, body { width: 1200px; height: 1012px; overflow: hidden; background: var(--paper); }
  body { position: relative; font-family: "Oswald", "Arial Narrow", sans-serif; color: var(--ink); }

  .brand-mark {
    position: absolute; left: 519px; top: 40px; width: 165px; height: 165px;
    background: var(--ink); border: 7px solid var(--paper);
    outline: 3px solid var(--gold); box-shadow: 0 0 0 3px var(--gold);
  }
  .site-title {
    position: absolute; left: 0; width: 1200px; top: 216px; text-align: center;
    font-weight: 400; font-size: 34px; letter-spacing: 1px;
  }
  .rule {
    position: absolute; left: 40px; width: 1120px; height: 2px;
    background: linear-gradient(90deg, rgba(189,182,142,0) 0%, var(--gold) 30%, var(--gold) 70%, rgba(189,182,142,0) 100%);
  }
  .main-nav {
    position: absolute; top: 290px; left: 0; width: 1200px;
    display: flex; justify-content: center; gap: 58px;
    font-size: 20px; font-weight: 300; letter-spacing: 1px; text-transform: uppercase;
  }
  .main-nav a { color: var(--ink); text-decoration: none; }
  .main-nav a.is-current { color: var(--accent); }

  .frame {
    position: absolute; background: var(--mat);
    border: 20px solid var(--wood);
    border-top-color: #3a1c0c; border-left-color: #42210f;
    border-bottom-color: var(--wood-light); border-right-color: #5a3219;
    box-shadow: inset 0 0 0 3px #d9d9d9, 0 2px 4px rgba(0,0,0,.25);
  }
  .frame--left { left: 39px; top: 461px; width: 351px; height: 276px; }
  .frame--center { left: 450px; top: 401px; width: 299px; height: 398px; }
  .frame--right { left: 810px; top: 461px; width: 351px; height: 276px; }
  .artwork { position: absolute; }
  .frame--left .artwork { left: 21px; top: 20px; right: 21px; bottom: 22px;
    background: radial-gradient(circle at 55% 50%, #f4f0e4 0%, #d9a62a 35%, #c24d1f 60%, #8fc1e0 100%); }
  .frame--center .artwork { left: 24px; top: 26px; right: 24px; bottom: 26px;
    background: linear-gradient(160deg, #2fa4c9 0%, #d9882f 35%, #3b9a86 60%, #2d3b2f 85%, #e7e3dc 100%); }
  .frame--right .artwork { left: 21px; top: 20px; right: 21px; bottom: 22px;
    background: linear-gradient(120deg, #4a1f1a 0%, #c99a94 40%, #efe9ea 60%, #8c4a4a 100%); }

  .social-links {
    position: absolute; top: 879px; left: 0; width: 1200px;
    display: flex; justify-content: center; gap: 30px;
    font-size: 15px; font-weight: 400;
  }
  .social-links a { color: var(--ink); text-decoration: none; }
  .copyright {
    position: absolute; top: 939px; left: 0; width: 1200px; text-align: center;
    font-size: 17px; font-weight: 300; letter-spacing: .5px;
  }
</style>
</head>
<body>
  <header>
    <div class="brand-mark" aria-hidden="true"></div>
    <h1 class="site-title">Marlena Voskuijl</h1>
    <div class="rule" style="top:276px"></div>
    <nav class="main-nav">
      <a href="#" class="is-current">Home</a>
      <a href="#">About Me</a>
      <a href="#">Contact</a>
    </nav>
    <div class="rule" style="top:330px"></div>
  </header>

  <main class="gallery">
    <div class="frame frame--left"><div class="artwork" role="img" aria-label="Abstract painting in ochre, red and blue swirling strokes"></div></div>
    <div class="frame frame--center"><div class="artwork" role="img" aria-label="Abstract painting with turquoise, orange and dark burst of brushstrokes"></div></div>
    <div class="frame frame--right"><div class="artwork" role="img" aria-label="Abstract floral painting with dusty pink roses and dark leaves"></div></div>
  </main>

  <footer>
    <div class="social-links">
      <a href="#">Pagefolk</a>
      <a href="#">Chirrup</a>
      <a href="#">Lenscape</a>
    </div>
    <div class="rule" style="top:923px"></div>
    <p class="copyright">Copyright 2022, Marlena Vos</p>
    <div class="rule" style="top:977px"></div>
  </footer>
</body>
</html>
```